Business Card front and back

I am looking for business card design. I really really like the design file I uploaded named 627788_19250069_3478263_85f427ee_image

Target Market(s)

Corporate Fitness High end Private country club

Industry/Entity Type

Fitness Industry

Contact Information for Business Card

The last image I like as an example I uploaded a bunch of my logos. The file labeled "the signature" is my business card information for you to use

Colors
0054AA
0677BA
7BADD7
CADEEF
E8F1F8

Requirements
Must have
• E-mail sigThe file I uploaded labeled "627788_19250069_3478263_85f427ee_image" with all the plus signs on the back if those could be the logo symbol I uploaded labeled "1 back.png"

```html
<!DOCTYPE html>
<html lang="en">
<head>
<meta charset="utf-8">
<title>Peakform Studio – Business Card</title>
<link href="https://fonts.googleapis.com/css2?family=Source+Sans+3:wght@400;600&display=swap" rel="stylesheet">
<style>
  :root{
    --page:#e8e8e8;
    --card:#000000;
    --card-glow:#2a2a2c;
    --brand-blue:#4a7cc0;
    --text-light:#f2f2f2;
    --mark-dark:#1c1c1e;
    --mark-mid:#3a3a3d;
    --mark-light:#767678;
  }
  *{margin:0;padding:0;box-sizing:border-box}
  html,body{width:1200px;height:960px;overflow:hidden;background:var(--page)}
  body{position:relative;font-family:"Source Sans 3",Arial,sans-serif}

  .card{position:absolute;width:745px;height:426px;background:var(--card);overflow:hidden}
  .card--front{left:154px;top:37px;background:var(--card)}
  .card--back{left:318px;top:488px;
    background:radial-gradient(ellipse 360px 260px at 230px 120px,#1a1a1b,var(--card) 80%)}

  .front-pattern{position:absolute;inset:0;
    background:
      radial-gradient(ellipse 230px 230px at 373px 215px,rgba(48,48,52,.9),rgba(0,0,0,0) 100%),
      linear-gradient(90deg,#000 0%,#070707 30%,#151516 60%,#222224 100%)}

  .front-brand{position:absolute;left:0;right:0;top:184px;text-align:center}
  .front-brand__square{display:block;width:40px;height:40px;margin:0 auto 16px;background:var(--brand-blue)}
  .front-brand__name{font-weight:600;font-size:23px;letter-spacing:1px;color:var(--text-light)}

  .back-mark{position:absolute;left:342px;top:72px;width:376px;height:280px;border-radius:0 60px 60px 0;
    background:radial-gradient(ellipse 200px 160px at 310px 190px,var(--mark-light),var(--mark-mid) 45%,var(--mark-dark) 90%)}

  .person{position:absolute;left:46px;top:190px}
  .person__name{font-size:31px;font-weight:400;color:var(--brand-blue);line-height:1;letter-spacing:-.6px}
  .person__role{font-size:20px;color:var(--text-light);line-height:1.2;margin-top:2px}

  .contact{position:absolute;left:46px;top:277px;list-style:none}
  .contact__item{display:flex;align-items:center;height:31px;font-size:19px;color:var(--text-light)}
  .contact__icon{width:20px;height:20px;margin-right:10px;fill:var(--brand-blue)}
</style>
</head>
<body>
  <section class="card card--front">
    <div class="front-pattern" role="img" aria-label="Repeating faint brand symbol pattern"></div>
    <div class="front-brand">
      <span class="front-brand__square"></span>
      <span class="front-brand__name">PEAKFORM STUDIO</span>
    </div>
  </section>

  <section class="card card--back">
    <div class="back-mark" role="img" aria-label="Large brand symbol in graphite tones"></div>
    <div class="person">
      <h1 class="person__name">DANIEL HARMON</h1>
      <p class="person__role">consultant</p>
    </div>
    <ul class="contact">
      <li class="contact__item">
        <svg class="contact__icon" viewBox="0 0 20 20"><path d="M2 8l8-5 8 5v9H2z"/><path d="M4 9l6 4 6-4" fill="none" stroke="#000" stroke-width="1.5"/></svg>
        daniel@peakformstudio.com
      </li>
      <li class="contact__item">
        <svg class="contact__icon" viewBox="0 0 20 20"><g fill="none" stroke="#4a7cc0" stroke-width="1.4"><circle cx="10" cy="10" r="8"/><ellipse cx="10" cy="10" rx="3.5" ry="8"/><path d="M2 10h16M3.5 6h13M3.5 14h13"/></g></svg>
        www.peakformstudio.com
      </li>
      <li class="contact__item">
        <svg class="contact__icon" viewBox="0 0 20 20"><path d="M5 2l3 3-2 2.5c1 2.2 2.6 3.9 4.6 5L13 10l3 3-2.3 3C8 15.5 4.3 11.7 3 5z"/></svg>
        555-014-2876
      </li>
      <li class="contact__item">
        <svg class="contact__icon" viewBox="0 0 20 20"><path d="M10 1a6 6 0 0 1 6 6c0 4.5-6 12-6 12S4 11.5 4 7a6 6 0 0 1 6-6z"/><circle cx="10" cy="7" r="2.2" fill="#000"/></svg>
        OR. WA. ID. MT. WY. UT
      </li>
    </ul>
  </section>
</body>
</html>
```